Higher co-efficient of performance means more heat for your money

I need a bar graph that will have the following heating systems, 80% efficient gas furnace COP of .8, Electric heat COP of 1, and Our best selling heat pump with a cop of 4 at 47F. I will have a constant bar, 100$ worth of gas for furnace, 100$ of electricity for electric heat, and 100$ worth of electricity for our heat pumps. next to them I will have a bar showing how much heat each heating system will provide for $100 of fuel. For gas furnace I need a bar that says $80 worth of heat and the barograph to match it, for electric heat I need the bar to show 100$ worth of heat, for our best selling heat pump I need the bar graph to show and say $400 dollars worth of heat. Please take a look at my website www.brightmarkcomfort.example for brand color and feel

```html
<!DOCTYPE html>
<html lang="en">
<head>
<meta charset="utf-8">
<title>Higher Coefficient of Performance – Brightmark Comfort</title>
<link rel="stylesheet" href="https://fonts.googleapis.com/css2?family=Montserrat:wght@500;700;800&display=swap">
<style>
  :root {
    --brand-blue: #0370c0;
    --blue-dark: #0366b4;
    --blue-light: #0c7bc8;
    --brand-red: #e41c2a;
    --red-dark: #e11a28;
    --red-light: #e8323e;
    --white: #ffffff;
    --ink: #1a1a1a;
    --baseline: #b4b4b4;
  }
  * { margin: 0; padding: 0; box-sizing: border-box; }
  html, body { width: 1200px; height: 1200px; overflow: hidden; background: var(--white); }
  body { font-family: "Montserrat", Arial, sans-serif; position: relative; }

  .header-shape { position: absolute; left: 0; top: 0; width: 1200px; height: 360px; }

  .headline {
    position: absolute; left: 60px; top: 44px;
    color: var(--white); font-weight: 800; font-size: 36px; line-height: 47px;
    letter-spacing: 0.5px; text-transform: uppercase;
  }
  .footnote {
    position: absolute; left: 60px; top: 208px;
    color: var(--white); font-weight: 500; font-size: 24px; letter-spacing: 0.3px;
  }

  .brand {
    position: absolute; right: 84px; top: 150px;
    display: flex; align-items: center; gap: 18px;
  }
  .brand-dot { width: 46px; height: 46px; border-radius: 50%; background: var(--white); }
  .brand-name {
    color: var(--white); font-weight: 700; font-size: 38px; line-height: 42px;
    letter-spacing: 1px; text-transform: uppercase; text-align: left;
  }

  .baseline {
    position: absolute; left: 0; top: 1066px; width: 1200px; height: 4px;
    background: var(--baseline);
  }

  .bar {
    position: absolute; bottom: 132px; width: 106px;
    display: flex; flex-direction: column; align-items: center;
    color: var(--white); font-weight: 800; text-align: center; text-transform: uppercase;
  }
  .bar--spend { background: linear-gradient(90deg, var(--blue-dark) 50%, var(--blue-light) 50%); }
  .bar--heat { background: linear-gradient(90deg, var(--red-dark) 50%, var(--red-light) 50%); }
  .bar-value { font-size: 31px; line-height: 32px; }
  .bar-of { font-size: 14px; line-height: 16px; }
  .bar-unit { font-size: 21px; line-height: 24px; }

  .category {
    position: absolute; top: 1094px; width: 360px; margin-left: -180px;
    color: var(--ink); font-weight: 800; font-size: 30px; line-height: 34px;
    text-align: center; text-transform: uppercase;
  }
</style>
</head>
<body>

<svg class="header-shape" viewBox="0 0 1000 300" preserveAspectRatio="none" aria-hidden="true">
  <path d="M0 0 H1000 V212 C850 240 650 272 450 272 C260 272 110 256 0 242 Z" fill="var(--brand-blue)"/>
  <path d="M0 256 C150 272 300 284 480 282 C680 278 860 244 1000 224 L1000 244 C860 266 680 298 480 302 C300 304 140 296 0 290 Z" fill="var(--brand-red)"/>
</svg>

<h1 class="headline">Higher co-efficient of<br>performance means more<br>heat for your money</h1>
<p class="footnote">*COP MEASURE OF 47°F</p>

<div class="brand">
  <span class="brand-dot"></span>
  <span class="brand-name">Brightmark<br>Comfort</span>
</div>

<!-- Gas furnace -->
<div class="bar bar--spend" style="left:50px; height:272px; padding-top:80px;">
  <span class="bar-value">100</span><span class="bar-of">of</span><span class="bar-unit">Gas</span>
</div>
<div class="bar bar--heat" style="left:196px; height:212px; padding-top:52px;">
  <span class="bar-value">80</span><span class="bar-of">of</span><span class="bar-unit">Heat</span>
</div>

<!-- Electric heat -->
<div class="bar bar--spend" style="left:476px; height:272px; padding-top:74px;">
  <span class="bar-value">100</span><span class="bar-of">of</span><span class="bar-unit">Elect.</span>
</div>
<div class="bar bar--heat" style="left:629px; height:272px; padding-top:74px;">
  <span class="bar-value">100</span><span class="bar-of">of</span><span class="bar-unit">Heat</span>
</div>

<!-- Heat pump -->
<div class="bar bar--spend" style="left:868px; height:272px; padding-top:74px;">
  <span class="bar-value">100</span><span class="bar-of">of</span><span class="bar-unit">Elect.</span>
</div>
<div class="bar bar--heat" style="left:1014px; width:104px; height:566px; padding-top:84px;">
  <span class="bar-value">400</span><span class="bar-unit">Work</span><span class="bar-of">of</span><span class="bar-unit">Heat</span>
</div>

<div class="baseline"></div>

<p class="category" style="left:168px;">80%<br>Gas furnace</p>
<p class="category" style="left:606px;">Electric<br>heat</p>
<p class="category" style="left:990px; width:400px; margin-left:-200px;">Our best<br>selling heat pump</p>

</body>
</html>
```